Animal Eye Clinic needs a Business card

We are a new veterinary ophthalmology practice (Tessaly Animal Eye Care) and we need a business card designed. We only see animal eyes - we are not a regular veterinary clinic. We already have a logo. We are looking for a professional, good looking business card to hand out to our clients. We are looking for something simple but professional and contemporary. Our logo is likely the only picture/graphic that needs to be on the card.
Updates

Contact Information for Business Card

Marisol Dunkley, BSc, DVM, MSc, DipACVO
Veterinary Ophthalmologist

Phone: 250.418.3097
Email: tessalyanimaleyecare@mailbrook.net
Website: tessalyanimaleyecare.net
Address: 1840 Pellworth Rd
Kelowna, BC, V4T 8M3

Colors

Designer to choose colors to be used in the design.

Requirements
Must have
• Our logo (attached)

```html
<!DOCTYPE html>
<html lang="en">
<head>
<meta charset="utf-8">
<title>Tessaly Animal Eye Care – Business Card</title>
<link rel="stylesheet" href="https://fonts.googleapis.com/css2?family=Archivo:wght@400;700;800&family=Roboto+Condensed:wght@400;700&display=swap">
<style>
  :root {
    --teal: #1b97a9;
    --teal-deep: #168898;
    --teal-soft: #27a3b4;
    --ink: #5f6467;
    --rule: #6e6e6e;
    --paper: #ffffff;
    --stage: #e9ebec;
  }
  * { box-sizing: border-box; margin: 0; padding: 0; }
  html, body { width: 1200px; height: 900px; overflow: hidden; }
  body {
    background: var(--stage);
    font-family: "Roboto Condensed", "Arial Narrow", sans-serif;
    position: relative;
  }
  .card {
    position: absolute;
    left: 250px;
    width: 700px;
    height: 400px;
    overflow: hidden;
    box-shadow: 0 6px 18px rgba(0,0,0,.18);
  }
  /* Front */
  .card-front { top: 30px; background: var(--teal); }
  .front-texture {
    position: absolute; inset: 0;
    background: radial-gradient(ellipse at 50% 50%, var(--teal-soft) 0%, var(--teal) 55%, var(--teal-deep) 100%);
  }
  .front-mark {
    position: absolute; left: 0; right: 0; top: 50%;
    transform: translateY(-50%);
    display: flex; align-items: center; justify-content: center; gap: 14px;
    color: var(--paper);
    font-family: "Archivo", Arial, sans-serif;
    font-weight: 700;
    font-size: 26px;
    letter-spacing: .5px;
  }
  .mark-dot {
    width: 34px; height: 34px; border-radius: 50%;
    background: var(--paper);
  }
  /* Back */
  .card-back { top: 470px; background: var(--paper); }
  .brand-band {
    position: absolute; left: 0; top: 0; bottom: 0; width: 228px;
    background: var(--teal);
  }
  .band-rule {
    position: absolute; top: 0; bottom: 0; left: 238px; width: 11px;
    background: var(--rule);
  }
  .band-name {
    position: absolute;
    left: 114px; top: 200px;
    transform: translate(-50%, -50%) rotate(-90deg);
    white-space: nowrap;
    display: flex; align-items: center; gap: 12px;
    color: var(--paper);
    font-family: "Archivo", Arial, sans-serif;
    font-weight: 700;
    font-size: 24px;
    letter-spacing: .3px;
  }
  .band-name .mark-dot { width: 30px; height: 30px; }
  .contact {
    position: absolute; left: 312px; top: 92px;
    color: var(--ink);
  }
  .person-name {
    font-family: "Archivo", Arial, sans-serif;
    font-weight: 800;
    font-size: 34px;
    letter-spacing: 1px;
    color: var(--teal);
    line-height: 1;
  }
  .credentials {
    font-weight: 700; font-size: 17px; color: var(--teal);
    margin-top: 4px;
  }
  .role { font-size: 19px; margin-top: 2px; }
  .address { font-size: 19px; margin-top: 12px; line-height: 1.2; }
  .channels { list-style: none; margin-top: 12px; font-size: 19px; line-height: 1.35; }
  .channels li { display: flex; align-items: center; gap: 9px; }
  .channels svg { width: 19px; height: 19px; flex: none; }
</style>
</head>
<body>

<section class="card card-front" aria-label="Card front">
  <div class="front-texture" role="img" aria-label="Faint repeating pattern of animal head silhouettes in teal"></div>
  <div class="front-mark">
    <span class="mark-dot"></span>
    <span>Tessaly Animal Eye Care</span>
  </div>
</section>

<section class="card card-back" aria-label="Card back">
  <div class="brand-band">
    <div class="band-name">
      <span class="mark-dot"></span>
      <span>Tessaly Animal Eye Care</span>
    </div>
  </div>
  <div class="band-rule"></div>

  <div class="contact">
    <h1 class="person-name">MARISOL DUNKLEY</h1>
    <p class="credentials">BSc, DVM, MSc, DipACVO</p>
    <p class="role">Veterinary Ophthalmologist</p>
    <p class="address">1840 Pellworth Rd<br>Kelowna, BC, V4T 8M3</p>
    <ul class="channels">
      <li>
        <svg viewBox="0 0 20 20" fill="none" stroke="#1b97a9" stroke-width="1.6"><circle cx="10" cy="10" r="8.2"/><path d="M7.2 5.8l1.4 2.2-1 1.1c.6 1.3 1.6 2.3 2.9 2.9l1.1-1 2.2 1.4-.6 1.6c-3.6-.2-6.4-3-6.6-6.6z" fill="#1b97a9" stroke="none"/></svg>
        250.418.3097
      </li>
      <li>
        <svg viewBox="0 0 20 20" fill="none" stroke="#1b97a9" stroke-width="1.6"><rect x="2" y="4.5" width="16" height="11" rx="1"/><path d="M2.5 5l7.5 6 7.5-6"/></svg>
        tessalyanimaleyecare@mailbrook.net
      </li>
      <li>
        <svg viewBox="0 0 20 20" fill="none" stroke="#1b97a9" stroke-width="1.6"><circle cx="10" cy="10" r="8"/><ellipse cx="10" cy="10" rx="3.6" ry="8"/><path d="M2 10h16M3.3 6h13.4M3.3 14h13.4"/></svg>
        www.tessalyanimaleyecare.net
      </li>
    </ul>
  </div>
</section>

</body>
</html>
```